Zielgruppe
Über die KALV:
Die KALV ist eine med. Vereinigung in der sich Ärzte aus allen Fachrichtungen zum Thema Adipositas austauschen.
Als 'Kestrel Alliance for Lipid and Vital Health Research Network' sind wir seit 1996 ein Pionier in der Schweiz im Bereich der krankhaften Adipositas und Stoffwechselstörungen.
Unsere Mitglieder - ein Zusammenschluss von Fachleuten, die sich mit Adipositas befassen - arbeiten eng zusammen, um das Verständnis und die Behandlung dieser Krankheit zu verbessern.
Aufgabenstellung
Die Farben der Präsentation sollten sich an den Farben unseres neuen Logos halten. Bitte verwenden Sie bei der Erstellung der Folienlayouts eine Schrift die allgemein bereits in den Microsoft Programmen enthalten sind. Es soll ein modernes und minimallistisches Design sein. Es geht bei diesem Auftrag um ein Grundlayout von Präsentationsfolien welches unsere Mitglieder verwenden wenn diese Vorträge halten.

```html
<!DOCTYPE html>
<html lang="de">
<head>
<meta charset="utf-8">
<title>KALV – Folienvorlagen</title>
<link rel="stylesheet" href="https://fonts.googleapis.com/css2?family=Arimo:wght@400;700&display=swap">
<style>
:root{
  --blue:#4472b8;
  --red:#c8102e;
  --grey-bg:#cfcfcf;
  --panel:#e6e6e6;
  --text:#8a8a8a;
  --white:#fff;
}
*{margin:0;padding:0;box-sizing:border-box}
html,body{width:1200px;height:891px;overflow:hidden}
body{background:var(--grey-bg);font-family:"Arimo",Arial,sans-serif;position:relative}
.slide{position:absolute;width:339px;height:201px;background:var(--white);overflow:hidden}
.c0{left:66px}.c1{left:431px}.c2{left:795px}
.r0{top:27px}.r1{top:241px}.r2{top:455px}.r3{top:669px}
.abs{position:absolute}
.bar{position:absolute;left:0;right:0;bottom:0;height:5px;background:var(--red)}
.title{position:absolute;left:19px;top:12px;color:var(--blue);font-weight:700;font-size:15px;letter-spacing:1.2px;line-height:1}
.sub{position:absolute;left:19px;top:29px;color:var(--text);font-size:7px}
.brand{position:absolute;right:18px;bottom:7px;display:flex;align-items:center;gap:2px;color:var(--blue);font-weight:700;font-size:10px;line-height:1}
.brand i{display:block;width:6px;height:6px;background:var(--red)}
.brand.light{color:var(--white)}
.body{color:var(--text);font-size:5.6px;line-height:1.28;text-align:justify}
.photo{position:absolute}
.icon{fill:none;stroke:currentColor;stroke-width:1.6;stroke-linecap:round;stroke-linejoin:round}
.h6{color:var(--blue);font-weight:700;font-size:6.4px}
.tiny{color:var(--text);font-size:4.4px;line-height:1.25}
/* cover */
.cover-band{position:absolute;left:149px;top:110px;width:190px;height:40px;background:rgba(68,114,184,.85);color:var(--white);padding:2px 0 0 24px;line-height:1}
.cover-band b{display:block;font-size:21px;letter-spacing:2.5px;margin-bottom:4px}
.cover-band span{display:block;font-size:7px}
/* steps */
.step{position:absolute;width:60px;text-align:center;top:60px}
.step .n{color:var(--blue);font-weight:700;font-size:10px}
.pin{width:34px;height:46px;margin:1px auto 0;display:block}
/* table */
.tbl-head,.tbl-foot{position:absolute;left:31px;width:275px;height:16px;background:var(--blue);color:var(--white);font-size:4.6px;display:flex;align-items:center}
.tbl-head span,.tbl-foot span{position:absolute;transform:translateX(-50%)}
/* columns */
.col{position:absolute;top:0;width:67px;height:196px;background:var(--panel);text-align:center}
.col .num{color:var(--red);font-weight:700;font-size:10px;margin-top:19px}
.col .lab{color:var(--blue);font-weight:700;font-size:9.5px;letter-spacing:.6px;margin-top:11px}
.col .dl{color:var(--text);font-size:6px;line-height:12px;margin-top:8px}
.col .btn{display:inline-block;margin-top:12px;background:var(--blue);color:var(--white);font-size:3.6px;padding:4px 3px;width:36px}
.col.on{background:var(--blue)}
.col.on .num,.col.on .lab,.col.on .dl{color:var(--white)}
.col.on .btn{background:var(--white);color:var(--red);font-size:5.5px;width:44px;padding:5px 1px}
</style>
</head>
<body>
<svg width="0" height="0" style="position:absolute">
  <symbol id="i-clip" viewBox="0 0 20 20"><rect x="5" y="3.5" width="10" height="13" rx="1"/><path d="M8 3.5h4v2H8z M7.5 8.5h5 M7.5 11h5 M7.5 13.5h5"/></symbol>
  <symbol id="i-steth" viewBox="0 0 20 20"><path d="M6 3v5a3.5 3.5 0 0 0 7 0V3 M9.5 11.5v2a3 3 0 0 0 6 0v-2"/><circle cx="15.5" cy="10" r="1.5"/></symbol>
  <symbol id="i-scope" viewBox="0 0 20 20"><circle cx="7" cy="8" r="4"/><path d="M10 11l3 3"/><circle cx="15" cy="15" r="2"/></symbol>
  <symbol id="i-chart" viewBox="0 0 20 20"><path d="M6 14V9 M10 14V6 M14 14v-3"/></symbol>
  <symbol id="i-mail" viewBox="0 0 20 20"><rect x="3" y="5" width="14" height="10"/><path d="M3 5l7 6 7-6"/></symbol>
  <symbol id="i-pin" viewBox="0 0 20 20"><path d="M10 18s-5-6-5-10a5 5 0 0 1 10 0c0 4-5 10-5 10z"/><circle cx="10" cy="8" r="2"/></symbol>
  <symbol id="i-globe" viewBox="0 0 20 20"><circle cx="10" cy="10" r="6.5"/><path d="M3.5 10h13 M10 3.5c-3 3.5-3 9.5 0 13 M10 3.5c3 3.5 3 9.5 0 13"/></symbol>
  <symbol id="i-home" viewBox="0 0 20 20"><path d="M3 10l7-6 7 6 M5 9v7h10V9 M8.5 16v-4h3v4"/></symbol>
  <symbol id="i-heart" viewBox="0 0 20 20"><path d="M10 17s-7-4.5-7-9a3.5 3.5 0 0 1 7-1 3.5 3.5 0 0 1 7 1c0 4.5-7 9-7 9z"/></symbol>
</svg>

<!-- 1 Title slide -->
<section class="slide c0 r0">
  <div class="photo" role="img" aria-label="Photo of two people cycling under a blue sky" style="left:0;top:0;width:339px;height:163px;background:linear-gradient(160deg,#9cc2e8 0%,#6fa0d6 45%,#c9c9c9 75%,#d86a3a 100%)"></div>
  <div class="cover-band"><b>HEADLINE</b><span>Lorem ipsum dolor sit amet, consectetuer</span></div>
  <div class="abs" style="left:0;top:163px;width:339px;height:2px;background:var(--red)"></div>
  <div class="abs" style="left:16px;top:171px;display:flex;align-items:center;gap:3px;color:var(--blue);font-weight:700;font-size:13px"><i style="display:block;width:9px;height:9px;background:var(--red)"></i>KALV</div>
  <div class="abs" style="left:16px;top:185px;color:var(--blue);font-size:5.4px;width:110px;line-height:1.2">Kestrel Alliance for Lipid and Vital Health Research Network</div>
</section>

<!-- 2 Text slide -->
<section class="slide c1 r0">
  <div class="title">LOREM IPSUM</div><div class="sub">Lorem ipsum dolor sit amet, consectetuer</div>
  <p class="body abs" style="left:19px;top:67px;width:303px">Lorem ipsum dolor sit amet, consectetuer adipiscing elit, sed diam nonummy nibh euismod tincidunt ut laoreet dolore magna aliquam erat volutpat. Ut wisi enim ad minim veniam, quis nostrud exerci tation ullamcorper suscipit lobortis nisl ut aliquip ex ea commodo consequat. Duis autem vel eum iriure dolor in hendrerit in vulputate velit esse molestie consequat, vel illum dolore eu feugiat nulla facilisis at vero eros et accumsan et iusto odio dignissim qui blandit praesent luptatum zzril delenit augue duis dolore te feugait nulla facilisi.<br>Lorem ipsum dolor sit amet, cons ectetuer adipiscing elit, sed diam nonummy nibh euismod tincidunt ut laoreet dolore magna aliquam erat volutpat. Ut wisi enim ad minim veniam, quis nostrud exerci tation ullamcorper suscipit lobortis nisl ut aliquip ex ea commodo consequat.<br>Lorem ipsum dolor sit amet, consectetuer adipiscing elit, sed diam nonummy nibh euismod tincidunt ut laoreet dolore magna aliquam erat volutpat. Ut wisi enim ad minim veniam, quis nostrud exerci tation</p>
  <div class="brand"><i></i>KALV</div><div class="bar"></div>
</section>

<!-- 3 Contact slide -->
<section class="slide c2 r0">
  <div class="photo" role="img" aria-label="Portrait photo of a smiling doctor in a white coat" style="left:0;top:0;width:157px;height:201px;background:linear-gradient(120deg,#e9e6e2,#d9c2a4 45%,#f2f2f2)"></div>
  <div class="abs" style="left:157px;top:0;width:38px;height:201px;background:var(--blue)"></div>
  <div class="abs" style="left:164px;top:49px;width:25px;height:1px;background:#fff"></div>
  <div class="abs" style="left:164px;top:99px;width:25px;height:1px;background:#fff"></div>
  <div class="abs" style="left:164px;top:149px;width:25px;height:1px;background:#fff"></div>
  <div class="brand light" style="right:auto;left:107px"><i></i>KALV</div>
  <div class="abs" style="left:180px;top:14px;width:20px;height:22px;background:#fff;color:var(--red)"><svg class="icon" width="20" height="22" viewBox="0 -1 20 22"><use href="#i-mail"/></svg></div>
  <div class="abs" style="left:180px;top:64px;width:20px;height:22px;background:#fff;color:var(--red)"><svg class="icon" width="20" height="22" viewBox="0 -1 20 22"><use href="#i-pin"/></svg></div>
  <div class="abs" style="left:180px;top:115px;width:20px;height:22px;background:#fff;color:var(--red)"><svg class="icon" width="20" height="22" viewBox="0 -1 20 22"><use href="#i-globe"/></svg></div>
  <div class="abs" style="left:180px;top:165px;width:20px;height:22px;background:#fff;color:var(--red)"><svg class="icon" width="20" height="22" viewBox="0 -1 20 22"><use href="#i-home"/></svg></div>
  <div class="abs" style="left:224px;top:19px;width:100px"><div class="h6">LOREM IPSUM</div><div class="tiny">Lorem ipsum dolor sit amet, consectetuer adipiscing elit, sed diam nonummy nibh</div></div>
  <div class="abs" style="left:224px;top:69px;width:100px"><div class="h6">LOREM IPSUM</div><div class="tiny">Lorem ipsum dolor sit amet, consectetuer adipiscing elit, sed diam nonummy nibh</div></div>
  <div class="abs" style="left:224px;top:119px;width:100px"><div class="h6">LOREM IPSUM</div><div class="tiny">Lorem ipsum dolor sit amet, consectetuer adipiscing elit, sed diam nonummy nibh</div></div>
  <div class="abs" style="left:224px;top:170px;width:100px"><div class="h6">LOREM IPSUM</div><div class="tiny">Lorem ipsum dolor sit amet, consectetuer adipiscing elit, sed diam nonummy nibh</div></div>
</section>

<!-- 4 Process steps -->
<section class="slide c0 r1">
  <div class="title">LOREM IPSUM</div><div class="sub">Lorem ipsum dolor sit amet, consectetuer</div>
  <div class="abs" style="left:60px;top:117px;width:218px;height:1px;background:#9aa9c4"></div>
  <div class="step" style="left:30px"><div class="n">1</div><svg class="pin" viewBox="0 0 34 46"><circle cx="17" cy="17" r="16" fill="#4472b8"/><path d="M10 29l7 12 7-12z" fill="#bbb"/><circle cx="17" cy="45" r="1.5" fill="#c8102e"/><svg x="7" y="7" width="20" height="20" class="icon" style="color:#fff"><use href="#i-clip"/></svg></svg></div>
  <div class="step" style="left:103px"><div class="n">2</div><svg class="pin" viewBox="0 0 34 46"><circle cx="17" cy="17" r="16" fill="#4472b8"/><path d="M10 29l7 12 7-12z" fill="#bbb"/><circle cx="17" cy="45" r="1.5" fill="#c8102e"/><svg x="7" y="7" width="20" height="20" class="icon" style="color:#fff"><use href="#i-steth"/></svg></svg></div>
  <div class="step" style="left:175px"><div class="n">3</div><svg class="pin" viewBox="0 0 34 46"><circle cx="17" cy="17" r="16" fill="#4472b8"/><path d="M10 29l7 12 7-12z" fill="#bbb"/><circle cx="17" cy="45" r="1.5" fill="#c8102e"/><svg x="7" y="7" width="20" height="20" class="icon" style="color:#fff"><use href="#i-scope"/></svg></svg></div>
  <div class="step" style="left:248px"><div class="n">4</div><svg class="pin" viewBox="0 0 34 46"><circle cx="17" cy="17" r="16" fill="#4472b8"/><path d="M10 29l7 12 7-12z" fill="#bbb"/><circle cx="17" cy="45" r="1.5" fill="#c8102e"/><rect x="9" y="12" width="16" height="11" fill="#fff"/><path d="M17 14v7M13.5 17.5h7" stroke="#c8102e" stroke-width="2"/></svg></div>
  <div class="abs" style="left:30px;top:126px;width:60px;text-align:center"><div class="h6">LOREM IPSUM</div><div class="tiny">Lorem ipsum dolor sit amet, consectetuer adipiscing elit, sed diam nonummy nibh</div></div>
  <div class="abs" style="left:103px;top:126px;width:60px;text-align:center"><div class="h6">LOREM IPSUM</div><div class="tiny">Lorem ipsum dolor sit amet, consectetuer adipiscing elit, sed diam nonummy nibh</div></div>
  <div class="abs" style="left:175px;top:126px;width:60px;text-align:center"><div class="h6">LOREM IPSUM</div><div class="tiny">Lorem ipsum dolor sit amet, consectetuer adipiscing elit, sed diam nonummy nibh</div></div>
  <div class="abs" style="left:248px;top:126px;width:60px;text-align:center"><div class="h6">LOREM IPSUM</div><div class="tiny">Lorem ipsum dolor sit amet, consectetuer adipiscing elit, sed diam nonummy nibh</div></div>
  <div class="brand"><i></i>KALV</div><div class="bar"></div>
</section>

<!-- 5 Chart slide -->
<section class="slide c1 r1">
  <div class="title">LOREM IPSUM</div><div class="sub">Lorem ipsum dolor sit amet, consectetuer</div>
  <svg class="abs" style="left:0;top:0" width="170" height="201" viewBox="0 0 170 201" font-family="Arimo, Arial, sans-serif">
    <g stroke="#d8d8d8" stroke-width=".5">
      <line x1="33" y1="84" x2="157" y2="84"/><line x1="33" y1="90" x2="157" y2="90"/><line x1="33" y1="96" x2="157" y2="96"/><line x1="33" y1="102" x2="157" y2="102"/><line x1="33" y1="109" x2="157" y2="109"/><line x1="33" y1="115" x2="157" y2="115"/><line x1="33" y1="121" x2="157" y2="121"/><line x1="33" y1="127" x2="157" y2="127"/><line x1="33" y1="133" x2="157" y2="133"/><line x1="33" y1="140" x2="157" y2="140"/><line x1="33" y1="146" x2="157" y2="146"/>
    </g>
    <g font-size="3.6" fill="#888" text-anchor="end">
      <text x="22" y="86">100</text><text x="22" y="92">90</text><text x="22" y="98">80</text><text x="22" y="104">70</text><text x="22" y="111">60</text><text x="22" y="117">50</text><text x="22" y="123">40</text><text x="22" y="129">30</text><text x="22" y="135">20</text><text x="22" y="142">10</text><text x="22" y="148">0</text>
    </g>
    <g font-size="5.5" fill="#4472b8" text-anchor="middle"><text x="34" y="157">1</text><text x="64" y="157">2</text><text x="94" y="157">3</text><text x="125" y="157">4</text><text x="155" y="157">5</text></g>
    <polyline points="34,120 64,126 94,112 125,113 155,93" fill="none" stroke="#c8102e" stroke-width=".9"/>
    <g fill="#c8102e"><circle cx="34" cy="120" r="1.6"/><circle cx="64" cy="126" r="1.6"/><circle cx="94" cy="112" r="1.6"/><circle cx="125" cy="113" r="1.6"/><circle cx="155" cy="93" r="1.6"/></g>
    <g fill="#4472b8">
      <circle cx="34" cy="105" r="6.5"/><circle cx="64" cy="111" r="6.5"/><circle cx="94" cy="97" r="6.5"/><circle cx="125" cy="98" r="6.5"/><circle cx="155" cy="78" r="6.5"/>
    </g>
    <g class="icon" style="color:#fff" stroke-width="1.3">
      <svg x="28" y="99" width="12" height="12"><use href="#i-clip"/></svg>
      <svg x="58" y="105" width="12" height="12"><use href="#i-steth"/></svg>
      <svg x="88" y="91" width="12" height="12"><use href="#i-scope"/></svg>
      <svg x="149" y="72" width="12" height="12"><use href="#i-chart"/></svg>
    </g>
    <rect x="120.5" y="95" width="9" height="6.5" fill="#fff"/><path d="M125 96.3v4M123 98.3h4" stroke="#c8102e" stroke-width="1.1"/>
  </svg>
  <p class="body abs" style="left:177px;top:70px;width:145px">Lorem ipsum dolor sit amet, consectetuer adipiscing elit, sed diam nonummy nibh euismod tincidunt ut laoreet dolore magna aliquam erat volutpat. Ut wisi enim ad minim veniam, quis nostrud exerci tation ullamcorper suscipit lobortis nisl ut aliquip ex ea commodo consequat. Duis autem vel eum iriure dolor in hendrerit in vulputate velit esse molestie consequat, vel illum dolore eu feugiat nulla facilisis at vero eros et accumsan et iusto odio dignissim qui blandit praesent luptatum zzril delenit augue duis dolore te feugait nulla facilisi.</p>
  <div class="brand"><i></i>KALV</div><div class="bar"></div>
</section>

<!-- 6 Table slide -->
<section class="slide c2 r1">
  <div class="title">LOREM IPSUM</div><div class="sub">Lorem ipsum dolor sit amet, consectetuer</div>
  <div class="abs" style="left:31px;top:49px;width:275px;height:121px;background:#f7f7f7"></div>
  <div class="abs" style="left:31px;top:65px;width:78px;height:89px;background:#efefef"></div>
  <div class="tbl-head" style="top:49px"><span style="left:33px">dolor sit amet</span><span style="left:96px">dolor sit amet</span><span style="left:146px">dolor sit amet</span><span style="left:195px">dolor sit amet</span><span style="left:245px">dolor sit amet</span></div>
  <div class="abs tiny" style="left:42px;top:75px;line-height:16.5px;font-size:4.2px;color:#999">Lorem ipsum dolor sit amet,<br>Lorem ipsum dolor sit amet,<br>Lorem ipsum dolor sit amet,<br>Lorem ipsum dolor sit amet,<br>Lorem ipsum dolor sit amet,</div>
  <svg class="abs" style="left:0;top:0" width="339" height="201">
    <g fill="#4472b8"><circle cx="133" cy="77" r="5"/><circle cx="133" cy="94" r="5"/>
      <circle cx="182" cy="77" r="5"/><circle cx="182" cy="94" r="5"/><circle cx="182" cy="110" r="5"/>
      <circle cx="232" cy="77" r="5"/><circle cx="232" cy="94" r="5"/><circle cx="232" cy="110" r="5"/><circle cx="232" cy="127" r="5"/></g>
    <g fill="#c8102e"><circle cx="281" cy="77" r="5"/><circle cx="281" cy="94" r="5"/><circle cx="281" cy="110" r="5"/><circle cx="281" cy="127" r="5"/><circle cx="281" cy="143" r="5"/></g>
  </svg>
  <div class="tbl-foot" style="top:154px"><span style="left:33px">dolor sit amet</span><span style="left:103px">it amet</span><span style="left:145px">dolor sit amet</span><span style="left:194px">dolor sit amet</span><span style="left:244px">dolor sit amet</span></div>
  <div class="brand"><i></i>KALV</div><div class="bar"></div>
</section>

<!-- 7 Blue feature slide -->
<section class="slide c0 r2" style="background:var(--blue)">
  <div class="title" style="color:#fff;left:25px;top:15px">LOREM IPSUM</div><div class="sub" style="color:#e6ecf6;left:25px;top:32px">Lorem ipsum dolor sit amet, consectetuer</div>
  <div class="abs" style="left:33px;top:62px;width:67px;height:39px;background:var(--panel);color:var(--red)"><svg class="icon" style="margin:10px 0 0 22px" width="22" height="22"><use href="#i-clip"/></svg></div>
  <div class="abs" style="left:101px;top:62px;width:67px;height:39px;background:var(--panel);color:var(--red)"><svg class="icon" style="margin:10px 0 0 22px" width="22" height="22"><use href="#i-steth"/></svg></div>
  <div class="abs" style="left:169px;top:62px;width:67px;height:39px;background:var(--panel);color:var(--red)"><svg class="icon" style="margin:10px 0 0 22px" width="22" height="22"><use href="#i-scope"/></svg></div>
  <div class="abs" style="left:237px;top:62px;width:67px;height:39px;background:var(--panel)"><svg style="margin:9px 0 0 23px" width="22" height="22" viewBox="0 0 20 20"><path d="M7.5 6V4h5v2" fill="none" stroke="#c8102e" stroke-width="1.4"/><rect x="3" y="6" width="14" height="10" fill="#c8102e"/><path d="M10 8.5v5M7.5 11h5" stroke="#fff" stroke-width="1.6"/></svg></div>
  <svg class="abs" style="left:0;top:101px" width="339" height="7"><g fill="#e6e6e6"><path d="M55 0h24l-12 6z"/><path d="M123 0h24l-12 6z"/><path d="M191 0h24l-12 6z"/><path d="M259 0h24l-12 6z"/></g></svg>
  <div class="abs" style="left:33px;top:117px;width:67px;text-align:center;color:#fff"><div style="font-weight:700;font-size:6.2px">LOREM IPSUM</div><div style="font-size:4.4px">Lorem ipsum dolor sit amet, consectetuer</div></div>
  <div class="abs" style="left:101px;top:117px;width:67px;text-align:center;color:#fff"><div style="font-weight:700;font-size:6.2px">LOREM IPSUM</div><div style="font-size:4.4px">Lorem ipsum dolor sit amet, consectetuer</div></div>
  <div class="abs" style="left:169px;top:117px;width:67px;text-align:center;color:#fff"><div style="font-weight:700;font-size:6.2px">LOREM IPSUM</div><div style="font-size:4.4px">Lorem ipsum dolor sit amet, consectetuer</div></div>
  <div class="abs" style="left:237px;top:117px;width:67px;text-align:center;color:#fff"><div style="font-weight:700;font-size:6.2px">LOREM IPSUM</div><div style="font-size:4.4px">Lorem ipsum dolor sit amet, consectetuer</div></div>
  <p class="body abs" style="left:32px;top:146px;width:273px;color:#e3e9f4;font-size:6px;text-align:left">Lorem ipsum dolor sit amet, consectetuer adipiscing elit, sed diam nonummy nibh euismod tincidunt ut laoreet dolore magna aliquam erat volutpat. Ut wisi enim ad minim veniam, quis nostrud exerci tation ullamcorper suscipit lobortis nisl ut aliquip ex ea commodo consequat. Duis autem vel eum iriure dolor in hendrerit in vulputate velit esse molestie consequat, vel illum dolore eu feugiat nulla</p>
  <div class="brand light" style="bottom:8px"><i style="background:#fff"></i>KALV</div>
  <div class="abs" style="left:0;right:0;bottom:0;height:3px;background:#fff"></div>
</section>

<!-- 8 Cross diagram -->
<section class="slide c1 r2">
  <div class="title">LOREM IPSUM</div><div class="sub">Lorem ipsum dolor sit amet, consectetuer</div>
  <div class="abs" style="left:149px;top:61px;width:33px;height:102px;background:var(--red)"></div>
  <div class="abs" style="left:114px;top:94px;width:103px;height:35px;background:var(--red)"></div>
  <div class="abs" style="left:149px;top:67px;width:33px;text-align:center;color:#fff;font-weight:700;font-size:15px">1</div>
  <div class="abs" style="left:183px;top:102px;width:33px;text-align:center;color:#fff;font-weight:700;font-size:15px">2</div>
  <div class="abs" style="left:149px;top:136px;width:33px;text-align:center;color:#fff;font-weight:700;font-size:15px">3</div>
  <div class="abs" style="left:115px;top:102px;width:33px;text-align:center;color:#fff;font-weight:700;font-size:15px">4</div>
  <svg class="abs" style="left:152px;top:98px" width="27" height="27" viewBox="0 0 20 20"><use href="#i-heart" fill="#fff"/><path d="M4 10h3l1.5-3 2 6 1.5-3h4" fill="none" stroke="#c8102e" stroke-width="1"/></svg>
  <div class="abs" style="left:192px;top:66px;width:80px"><div class="h6">LOREM IPSUM</div><div class="tiny">Lorem ipsum dolor sit amet, consectetuer adipiscing elit, sed diam nonummy nibh</div></div>
  <div class="abs" style="left:228px;top:101px;width:80px"><div class="h6">LOREM IPSUM</div><div class="tiny">Lorem ipsum dolor sit amet, consectetuer adipiscing elit, sed diam nonummy nibh</div></div>
  <div class="abs" style="left:68px;top:137px;width:73px;text-align:right"><div class="h6">LOREM IPSUM</div><div class="tiny">Lorem ipsum dolor sit amet, consectetuer adipiscing elit, sed diam nonummy nibh</div></div>
  <div class="abs" style="left:33px;top:102px;width:73px;text-align:right"><div class="h6">LOREM IPSUM</div><div class="tiny">Lorem ipsum dolor sit amet, consectetuer adipiscing elit, sed diam nonummy nibh</div></div>
  <div class="brand"><i></i>KALV</div><div class="bar"></div>
</section>

<!-- 9 Five columns -->
<section class="slide c2 r2" style="background:#fff">
  <div class="col" style="left:0"><div class="num">01</div><svg width="24" height="30" viewBox="0 0 24 30" style="margin-top:8px"><circle cx="12" cy="11" r="10" fill="#4472b8"/><path d="M8 19l4 8 4-8z" fill="#bbb"/><svg x="4" y="3" width="16" height="16" class="icon" style="color:#fff"><use href="#i-clip"/></svg></svg><div class="lab">LOREM</div><div class="dl">DOLOR<br>SIT<br>AMET</div><div class="btn">dolor sit amet,</div></div>
  <div class="col" style="left:68px"><div class="num">02</div><svg width="24" height="30" viewBox="0 0 24 30" style="margin-top:8px"><circle cx="12" cy="11" r="10" fill="#4472b8"/><path d="M8 19l4 8 4-8z" fill="#bbb"/><svg x="4" y="3" width="16" height="16" class="icon" style="color:#fff"><use href="#i-steth"/></svg></svg><div class="lab">LOREM</div><div class="dl">DOLOR<br>SIT<br>AMET</div><div class="btn">dolor sit amet,</div></div>
  <div class="col on" style="left:136px"><div class="num" style="font-size:13px;margin-top:15px">03</div><svg width="30" height="36" viewBox="0 0 30 36" style="margin-top:6px"><circle cx="15" cy="14" r="13" fill="#fff"/><path d="M10 24l5 10 5-10z" fill="#d5d5d5"/><svg x="5" y="4" width="20" height="20" class="icon" style="color:#c8102e"><use href="#i-scope"/></svg></svg><div class="lab" style="margin-top:8px;font-size:10.5px">LOREM</div><div class="dl">DOLOR<br>SIT<br>AMET</div><div class="btn">dolor sit amet,</div></div>
  <div class="col" style="left:205px"><div class="num">04</div><svg width="24" height="30" viewBox="0 0 24 30" style="margin-top:8px"><circle cx="12" cy="11" r="10" fill="#4472b8"/><path d="M8 19l4 8 4-8z" fill="#bbb"/><rect x="6" y="7" width="12" height="8" fill="#fff"/><path d="M12 8.5v5M9.5 11h5" stroke="#c8102e" stroke-width="1.4"/></svg><div class="lab">LOREM</div><div class="dl">DOLOR<br>SIT<br>AMET</div><div class="btn">dolor sit amet,</div></div>
  <div class="col" style="left:273px;width:66px"><div class="num">05</div><svg width="24" height="30" viewBox="0 0 24 30" style="margin-top:8px"><circle cx="12" cy="11" r="10" fill="#4472b8"/><path d="M8 19l4 8 4-8z" fill="#bbb"/><svg x="4" y="3" width="16" height="16" class="icon" style="color:#fff" stroke-width="2"><use href="#i-chart"/></svg></svg><div class="lab">LOREM</div><div class="dl">DOLOR<br>SIT<br>AMET</div><div class="btn">dolor sit amet,</div></div>
  <div class="brand"><i></i>KALV</div><div class="bar"></div>
</section>

<!-- 10 Text with portrait -->
<section class="slide c0 r3">
  <div class="title">LOREM IPSUM</div><div class="sub">Lorem ipsum dolor sit amet, consectetuer</div>
  <p class="body abs" style="left:18px;top:68px;width:144px;font-size:6px">Lorem ipsum dolor sit amet, consectetuer adipiscing elit, sed diam nonummy nibh euismod tincidunt ut laoreet dolore magna aliquam erat volutpat. Ut wisi enim ad minim veniam, quis nostrud exerci tation ullamcorper suscipit lobortis nisl ut aliquip ex ea commodo consequat. Duis autem vel eum iriure dolor in hendrerit in vulputate velit esse molestie consequat, vel illum dolore eu feugiat nulla facilisis at vero eros et accumsan et iusto odio dignissim qui blandit praesent luptatum zzril delenit augue duis dolore te feugait nulla facilisi.</p>
  <div class="photo" role="img" aria-label="Photo of a male doctor with stethoscope holding a folder" style="left:184px;top:0;width:155px;height:196px;background:linear-gradient(110deg,#a9c7e6,#e4edf5 50%,#7aa6d2)"></div>
  <div class="brand light"><i style="background:var(--red)"></i>KALV</div><div class="bar"></div>
</section>

<!-- 11 Two images -->
<section class="slide c1 r3">
  <div class="title">LOREM IPSUM</div><div class="sub">Lorem ipsum dolor sit amet, consectetuer</div>
  <div class="photo" role="img" aria-label="Photo of a red apple on a light grey surface" style="left:0;top:48px;width:170px;height:81px;background:linear-gradient(180deg,#d9d9d9,#ececec)"></div>
  <div class="photo" role="img" aria-label="Photo of blue and white medicine capsules" style="left:183px;top:48px;width:156px;height:81px;background:linear-gradient(135deg,#ffffff 0%,#eef4fb 55%,#d7e6f6 100%)"></div>
  <p class="body abs" style="left:13px;top:142px;width:145px">Lorem ipsum dolor sit amet, consectetuer adipiscing elit, sed diam nonummy nibh euismod tincidunt ut laoreet dolore magna aliquam erat volutpat. Ut wisi enim ad minim veniam, quis nostrud exerci tation ullamcorper suscipit lobortis</p>
  <p class="body abs" style="left:183px;top:142px;width:145px">Lorem ipsum dolor sit amet, consectetuer adipiscing elit, sed diam nonummy nibh euismod tincidunt ut laoreet dolore magna aliquam erat volutpat. Ut wisi enim ad minim veniam, quis nostrud exerci tation ullamcorper suscipit lobortis</p>
  <div class="brand"><i></i>KALV</div><div class="bar"></div>
</section>

<!-- 12 Quote -->
<section class="slide c2 r3">
  <div class="title">LOREM IPSUM</div><div class="sub">Lorem ipsum dolor sit amet, consectetuer</div>
  <div class="abs" style="left:54px;top:60px;width:36px;height:110px;background:var(--red)"></div>
  <div class="abs" style="left:18px;top:95px;width:72px;height:47px;background:var(--red)"></div>
  <div class="abs" style="left:59px;top:63px;color:#fff;font-weight:700;font-size:40px;line-height:1">“</div>
  <p class="abs" style="left:101px;top:94px;width:225px;color:var(--blue);font-size:9px;line-height:1.17;letter-spacing:.2px">LOREM IPSUM DOLOR SIT AMET, CONSECTE-TUER ADIPISCING ELIT, SED DIAM NONUMMY NIBH EUISMOD TINCIDUNT UT LAOREET DOLORE MAGNA.</p>
  <div class="brand"><i></i>KALV</div><div class="bar"></div>
</section>
</body>
</html>
```